Pomar Veloz - Working hours register App needs interface design

Pomar Veloz, a 1 million users Brazilian website focused on general calculations needs an interface to an App for registering the working hours of a housemaid, a nanny, a housekeeper or other domestic workers.
The final users should be mainly housewifes.
The wireframe of the pages is in the Tirvel_layout.xls file attached.
Logo is also available in the wireframe.
The interface should be optimized for Android on Nimbus QX with a 5'' screen.
Target Market(s)
Females, educated, from 30 to 50 y.o.
Industry/Entity Type
Android

```html
<!DOCTYPE html>
<html lang="en">
<head>
<meta charset="utf-8">
<title>Pomar Veloz – Tirvel</title>
<link href="https://fonts.googleapis.com/css2?family=Ubuntu:wght@300;400;500;700&display=swap" rel="stylesheet">
<style>
  :root {
    --bg: #161718;
    --bg-deep: #101112;
    --header-bg: #18191b;
    --header-line: #222326;
    --brand-red: #e0121b;
    --brand-red-dark: #b80a10;
    --text: #ffffff;
    --text-soft: #e6e6e6;
    --row-top: #4a4b4d;
    --row-mid: #2e2f31;
    --row-bottom: #121314;
    --row-edge: #6a6a6e;
    --btn-face: #6b6c6e;
    --btn-face-dark: #4a4b4d;
    --btn-ring: #0c0c0d;
  }
  * { box-sizing: border-box; margin: 0; padding: 0; }
  html, body {
    width: 675px; height: 1200px; overflow: hidden;
    background: var(--bg);
    font-family: "Ubuntu", sans-serif;
  }
  .screen {
    position: relative; width: 675px; height: 1200px;
    background: linear-gradient(180deg, var(--bg) 0%, var(--bg-deep) 100%);
  }
  .app-header {
    position: absolute; left: 0; top: 0; width: 675px; height: 172px;
    background: var(--header-bg);
    border-bottom: 1px solid var(--header-line);
  }
  .brand-square {
    position: absolute; left: 28px; top: 38px; width: 113px; height: 113px;
    border-radius: 9px;
    background: linear-gradient(180deg, var(--brand-red) 0%, var(--brand-red-dark) 100%);
  }
  .brand-name {
    position: absolute; left: 162px; top: 63px;
    color: var(--text); font-weight: 500; font-size: 31px; letter-spacing: 0.5px;
    line-height: 1;
  }
  .brand-sub {
    position: absolute; left: 162px; top: 100px;
    color: var(--text-soft); font-weight: 300; font-size: 25px; letter-spacing: 0.5px;
    line-height: 1;
  }
  .icon-btn {
    position: absolute; width: 46px; height: 46px;
    border-radius: 7px;
    background: var(--btn-ring);
    border: 1px solid #3a3b3d;
    display: flex; align-items: center; justify-content: center;
  }
  .icon-btn .face {
    width: 36px; height: 36px; border-radius: 5px;
    background: linear-gradient(180deg, var(--btn-face) 0%, var(--btn-face-dark) 100%);
    border: 1px solid #8a8b8d;
    display: flex; align-items: center; justify-content: center;
  }
  .edit-btn { left: 588px; top: 67px; }
  .employee-list { position: absolute; left: 28px; top: 207px; width: 619px; }
  .employee-row {
    position: relative; height: 153px; margin-bottom: 9px;
    display: flex;
    border-top: 1px solid var(--row-edge);
  }
  .employee-photo { width: 154px; height: 152px; flex: none; border-right: 1px solid #000; }
  .employee-body {
    flex: 1; position: relative;
    background:
      radial-gradient(ellipse 60% 45% at 45% 0%, rgba(255,255,255,0.12), transparent 70%),
      linear-gradient(180deg, var(--row-top) 0%, var(--row-mid) 55%, var(--row-bottom) 100%);
  }
  .employee-name {
    position: absolute; left: 25px; top: 50%; transform: translateY(-50%);
    margin-top: 3px;
    color: var(--text); font-size: 31px; font-weight: 400;
  }
  .employee-row .icon-btn { left: 560px; top: 53px; }
  .photo-one { background: linear-gradient(160deg, #f4e4d6 0%, #c98a62 45%, #e05a2a 100%); }
  .photo-two { background: linear-gradient(160deg, #c79474 0%, #a8694b 50%, #3a2418 100%); }
  .photo-three { background: linear-gradient(160deg, #6b3b2c 0%, #c68c6c 50%, #4a3a3c 100%); }
  .photo-four { background: linear-gradient(160deg, #1a1a1a 0%, #9a9a9a 50%, #2a2a2a 100%); }
</style>
</head>
<body>
<div class="screen">
  <header class="app-header">
    <div class="brand-square"></div>
    <div class="brand-name">POMAR VELOZ</div>
    <div class="brand-sub">TIRVEL</div>
    <div class="icon-btn edit-btn" aria-label="Edit">
      <div class="face">
        <svg width="22" height="22" viewBox="0 0 24 24" fill="none" stroke="#fff" stroke-width="2" stroke-linejoin="round">
          <path d="M4 20l1.2-4.8L16 4.4l3.6 3.6L8.8 18.8z"/>
          <path d="M14 6.4l3.6 3.6"/>
        </svg>
      </div>
    </div>
  </header>

  <main class="employee-list">
    <div class="employee-row">
      <div class="employee-photo photo-one" role="img" aria-label="Photo of employee one"></div>
      <div class="employee-body">
        <span class="employee-name">Employee One</span>
      </div>
      <div class="icon-btn"><div class="face">
        <svg width="16" height="16" viewBox="0 0 16 16"><path d="M5 3l5 5-5 5" fill="none" stroke="#fff" stroke-width="2.6"/></svg>
      </div></div>
    </div>
    <div class="employee-row">
      <div class="employee-photo photo-two" role="img" aria-label="Photo of employee two"></div>
      <div class="employee-body">
        <span class="employee-name">Employee Two</span>
      </div>
      <div class="icon-btn"><div class="face">
        <svg width="16" height="16" viewBox="0 0 16 16"><path d="M5 3l5 5-5 5" fill="none" stroke="#fff" stroke-width="2.6"/></svg>
      </div></div>
    </div>
    <div class="employee-row">
      <div class="employee-photo photo-three" role="img" aria-label="Photo of employee three"></div>
      <div class="employee-body">
        <span class="employee-name">Employee Three</span>
      </div>
      <div class="icon-btn"><div class="face">
        <svg width="16" height="16" viewBox="0 0 16 16"><path d="M5 3l5 5-5 5" fill="none" stroke="#fff" stroke-width="2.6"/></svg>
      </div></div>
    </div>
    <div class="employee-row">
      <div class="employee-photo photo-four" role="img" aria-label="Photo of employee four"></div>
      <div class="employee-body">
        <span class="employee-name">Employee Four</span>
      </div>
      <div class="icon-btn"><div class="face">
        <svg width="16" height="16" viewBox="0 0 16 16"><path d="M5 3l5 5-5 5" fill="none" stroke="#fff" stroke-width="2.6"/></svg>
      </div></div>
    </div>
  </main>
</div>
</body>
</html>
```